xmas banner to be printed in High quality

We require a banner to be designed similar to the images attached,
The banner must be 6000 x 1168 in size.
It must read Contain "The Holly Lantern"
the banner must be very high quality with great artwork and a magic feel. it must stand out and sparkle with the chrismassy effect. this will be used as a shop sign

Industry/Entity Type

Shop

Colors

Designer to choose colors to be used in the design.

Requirements
Must have
• must be a very christmassy theme and must stand out to be of a VERY high Quality

```html
<!DOCTYPE html>
<html lang="en">
<head>
<meta charset="utf-8">
<title>The Holly Lantern – Shop Banner</title>
<link rel="stylesheet" href="https://fonts.googleapis.com/css2?family=Fredoka:wght@600;700&display=swap">
<style>
  :root {
    --paper: #ffffff;
    --red-light: #ec2530;
    --red-mid: #cc141e;
    --red-deep: #900a12;
    --title-white: #ffffff;
    --title-shadow: rgba(70, 0, 6, 0.6);
    --snow: rgba(255, 236, 226, 0.85);
    --snow-soft: rgba(255, 220, 210, 0.55);
    --greenery-dark: #1d5436;
    --greenery-light: #3f8a4c;
    --berry: #e8561a;
    --gold: #efc46a;
    --ginger: #d9a55a;
  }
  * { margin: 0; padding: 0; box-sizing: border-box; }
  html, body {
    width: 1200px;
    height: 266px;
    overflow: hidden;
    background: var(--paper);
  }
  .banner {
    position: relative;
    width: 1200px;
    height: 266px;
    background: var(--paper);
  }
  .banner-field {
    position: absolute;
    left: 18px;
    top: 18px;
    width: 1164px;
    height: 230px;
    overflow: hidden;
    background: radial-gradient(ellipse 55% 85% at 55% 40%, var(--red-light) 0%, var(--red-mid) 55%, var(--red-deep) 100%);
  }
  .snowfall {
    position: absolute;
    inset: 0;
    background-image:
      radial-gradient(circle, var(--snow) 0 1.3px, transparent 2px),
      radial-gradient(circle, var(--snow-soft) 0 1px, transparent 1.6px),
      radial-gradient(circle, var(--snow) 0 1.8px, transparent 2.4px),
      radial-gradient(circle, var(--snow-soft) 0 0.9px, transparent 1.4px);
    background-size: 47px 39px, 29px 33px, 83px 71px, 19px 23px;
    background-position: 5px 11px, 17px 3px, 40px 27px, 9px 14px;
  }
  .glow {
    position: absolute;
    border-radius: 50%;
    background: radial-gradient(circle, rgba(255, 250, 235, 0.95) 0%, rgba(255, 230, 200, 0.35) 25%, rgba(255, 200, 180, 0) 70%);
  }
  .glow-a { left: 120px; top: 20px; width: 60px; height: 60px; }
  .glow-b { left: 140px; top: 125px; width: 56px; height: 56px; }
  .glow-c { right: 40px; top: 10px; width: 60px; height: 60px; }
  .glow-d { right: 70px; top: 110px; width: 50px; height: 50px; }
  .decor {
    position: absolute;
    top: 0;
    height: 230px;
  }
  .decor-left {
    left: 0;
    width: 200px;
    background:
      radial-gradient(ellipse 45% 30% at 35% 88%, var(--berry) 0%, var(--berry) 55%, rgba(232, 86, 26, 0) 75%),
      radial-gradient(ellipse 70% 60% at 25% 38%, var(--greenery-light) 0%, var(--greenery-dark) 60%, rgba(29, 84, 54, 0) 80%),
      radial-gradient(circle at 80% 68%, var(--gold) 0%, var(--gold) 14%, rgba(239, 196, 106, 0) 26%);
  }
  .decor-right {
    right: 0;
    width: 220px;
    background:
      radial-gradient(ellipse 40% 50% at 40% 62%, var(--ginger) 0%, var(--ginger) 60%, rgba(217, 165, 90, 0) 78%),
      radial-gradient(circle at 78% 18%, var(--gold) 0%, var(--gold) 16%, rgba(239, 196, 106, 0) 30%),
      radial-gradient(circle at 85% 88%, var(--gold) 0%, var(--gold) 14%, rgba(239, 196, 106, 0) 28%),
      radial-gradient(ellipse 35% 45% at 92% 55%, var(--greenery-light) 0%, var(--greenery-dark) 55%, rgba(29, 84, 54, 0) 80%);
  }
  .shop-title {
    position: absolute;
    left: 0;
    right: 0;
    top: 0;
    height: 230px;
    font-family: "Fredoka", "Arial Rounded MT Bold", sans-serif;
    font-weight: 700;
    color: var(--title-white);
    text-transform: uppercase;
    text-shadow: 2px 5px 6px var(--title-shadow);
    line-height: 1;
    text-align: center;
  }
  .shop-title-small {
    position: absolute;
    left: 0;
    right: 0;
    top: 14px;
    font-size: 66px;
    letter-spacing: 1px;
  }
  .shop-title-large {
    position: absolute;
    left: 0;
    right: 0;
    top: 96px;
    font-size: 84px;
    letter-spacing: 2px;
  }
</style>
</head>
<body>
  <div class="banner">
    <div class="banner-field">
      <div class="snowfall" aria-hidden="true"></div>
      <div class="decor decor-left" role="img" aria-label="Pine branches, holly leaves, orange berries and a gold star"></div>
      <div class="decor decor-right" role="img" aria-label="Gingerbread figure with gold stars and holly leaves"></div>
      <span class="glow glow-a" aria-hidden="true"></span>
      <span class="glow glow-b" aria-hidden="true"></span>
      <span class="glow glow-c" aria-hidden="true"></span>
      <span class="glow glow-d" aria-hidden="true"></span>
      <h1 class="shop-title">
        <span class="shop-title-small">The</span>
        <span class="shop-title-large">Holly Lantern</span>
      </h1>
    </div>
  </div>
</body>
</html>
```